KVM Contracting services . Building and maintenance services, optic fibre installation

Business cards and logo design.I need a logo that I can use on business cards ,workwear and on my vehicles. I would like the KVM to be the main or larger text and contracting services to be the smaller or less important text.I like monograms, modern designs and repeating patterns symbols. I am also a Gemini and my favourite number is 22 so if this can be any inspiration to help with the design. Am thinking of the using German flag colours as a his is my family’s heritage. And the other 2 main colours I wear is black and white.But any ideas are appreciated.I do not need a design that is trade specific but a design that could be used for any business.

Target Market(s)

General public

Contact Information for Business Card

KVM Contracting Services ( front of business card)

(Back of business card)
Marcus Dellwood
0419274530
Maintenance services
Optic fibre and data installation

Logo Text

Logo can just be pattern or monogram or incorporate KVM . I like the gemini star sign and the number 22

Colors
ec1f27
000000
fbee3e
ffffff

Requirements
Must have
• Logo and KVM Contracting Services on the front of business card
Nice to have
• Possible use of German flag colours.
• Modern design.
• Design to be able to be used on black or white background as I want to put it on clothing

```html
<!DOCTYPE html>
<html lang="en">
<head>
<meta charset="utf-8">
<title>KVM Contracting Services – Business Card</title>
<link href="https://fonts.googleapis.com/css2?family=Roboto:wght@500;700;900&family=Open+Sans:wght@400&display=swap" rel="stylesheet">
<style>
  :root {
    --backdrop: #5c5c5c;
    --card-light: #f3f3f3;
    --card-dark: #151515;
    --brand-red: #ec1f27;
    --brand-yellow: #fbee3e;
    --ink: #111111;
    --white: #ffffff;
  }
  * { margin: 0; padding: 0; box-sizing: border-box; }
  html, body {
    width: 1200px; height: 900px; overflow: hidden;
    background: var(--backdrop);
  }
  .stage { position: relative; width: 1200px; height: 900px; }

  .card { position: absolute; top: 200px; width: 310px; height: 502px; }
  .card-front {
    left: 253px; background: var(--card-light);
    border-radius: 62px 0 62px 0;
  }
  .card-back {
    left: 627px; background: var(--card-dark);
    border-radius: 0 62px 0 62px;
  }

  .brand { position: absolute; left: 30px; top: 152px; display: flex; align-items: center; }
  .brand-mark { width: 64px; height: 64px; background: var(--ink); margin-right: 18px; }
  .brand-text { font-family: "Roboto", sans-serif; font-weight: 900; color: var(--brand-red); }
  .brand-name { display: block; font-size: 60px; line-height: 52px; letter-spacing: 8px; }
  .brand-tagline { display: block; font-size: 12.5px; line-height: 16px; letter-spacing: 0.2px; margin-top: 4px; }

  .contact { position: absolute; left: 32px; top: 360px; }
  .contact-name {
    font-family: "Roboto", sans-serif; font-weight: 700; font-size: 18px;
    color: var(--brand-red); line-height: 22px;
  }
  .contact-phone {
    font-family: "Open Sans", sans-serif; font-size: 18px; color: var(--ink);
    line-height: 24px; margin-top: 2px;
  }
  .contact-services {
    font-family: "Open Sans", sans-serif; font-size: 15px; color: var(--ink);
    line-height: 18px; margin-top: 12px; list-style: none;
  }

  .back-brand {
    position: absolute; inset: 0; display: flex; flex-direction: column;
    align-items: center; justify-content: center;
  }
  .back-mark { width: 120px; height: 120px; background: var(--brand-red); }
  .back-name {
    font-family: "Roboto", sans-serif; font-weight: 900; font-size: 44px;
    letter-spacing: 6px; color: var(--white); margin-top: 22px;
  }
</style>
</head>
<body>
<main class="stage">
  <section class="card card-front" aria-label="Business card front">
    <div class="brand">
      <span class="brand-mark"></span>
      <span class="brand-text">
        <span class="brand-name">KVM</span>
        <span class="brand-tagline">CONTRACTING SERVICES</span>
      </span>
    </div>
    <div class="contact">
      <p class="contact-name">MARCUS DELLWOOD</p>
      <p class="contact-phone">0419274530</p>
      <ul class="contact-services">
        <li>Maintenance services</li>
        <li>Optic fibre and data installation</li>
      </ul>
    </div>
  </section>

  <section class="card card-back" aria-label="Business card back">
    <div class="back-brand">
      <span class="back-mark"></span>
      <span class="back-name">KVM</span>
    </div>
  </section>
</main>
</body>
</html>
```